Instagram background for quotes

We need a 1080x1080 background for instagram. I use the Letrova app to put text over the image.

We create motivating and inspiring messages for our followers on IG.

Our brands message is, "Mediocre thinking leads to mediocre results. Get Mission - Get Motivated - Get Moving
https://www.instagram.com/steel_outlook/

We would like to move away from the rustic look and have a gloss black background with the goal of using text that is cleaner to match the SO in the logo.

I see the design remaining fairly close to what it is now with the logo at the top. I like the quotes on this brand here, https://www.instagram.com/quizatycoon/?hl=en. I see this being built into our new background with the quotations being aggressive to match the wings in our logo.

Here is another brand we like - https://www.instagram.com/zipzapdrive/

I've attached the files I was given by the logo designer who has disappeared. I am hoping what is there will suffice.

Target Market(s)

24-34 year old males

Industry/Entity Type

Quotes

Colors
000000
ffffff

Requirements
Must have
• Provided Logo without text
Nice to have
• Aggressive looking quotes to match wings
• Watermark logo in background

```html
<!DOCTYPE html>
<html lang="en">
<head>
<meta charset="utf-8">
<title>Steel Outlook – Quote Background</title>
<link href="https://fonts.googleapis.com/css2?family=Bebas+Neue&display=swap" rel="stylesheet">
<style>
  :root {
    --stage: #808080;
    --card: #000000;
    --ink: #ffffff;
  }
  html, body {
    margin: 0;
    padding: 0;
    width: 1200px;
    height: 1000px;
    overflow: hidden;
    background: var(--stage);
  }
  .canvas {
    position: relative;
    width: 1200px;
    height: 1000px;
  }
  .quote-card {
    position: absolute;
    left: 388px;
    top: 288px;
    width: 425px;
    height: 425px;
    background: var(--card);
    font-family: "Bebas Neue", "Oswald", sans-serif;
    color: var(--ink);
  }
  .quote-card__frame {
    position: absolute;
    inset: 0;
  }
  .quote-card__tag {
    position: absolute;
    top: 14px;
    left: 0;
    right: 0;
    text-align: center;
    font-size: 19px;
    letter-spacing: 0.5px;
    line-height: 24px;
  }
  .quote-card__quote {
    position: absolute;
    left: 0;
    right: 0;
    top: 128px;
    margin: 0;
    text-align: center;
    font-weight: 400;
    line-height: 1;
  }
  .quote-card__line {
    display: block;
  }
  .quote-card__line--lead {
    font-size: 66px;
  }
  .quote-card__line--join {
    font-size: 34px;
    margin: 4px 0 2px;
  }
  .quote-card__line--close {
    font-size: 68px;
  }
  .quote-card__brand {
    position: absolute;
    left: 0;
    right: 0;
    top: 378px;
    text-align: center;
    font-size: 40px;
    line-height: 40px;
    letter-spacing: 2px;
  }
</style>
</head>
<body>
  <main class="canvas">
    <section class="quote-card">
      <svg class="quote-card__frame" width="425" height="425" viewBox="0 0 425 425" aria-hidden="true">
        <g fill="none" stroke="#ffffff" stroke-width="2">
          <line x1="26" y1="26" x2="128" y2="26"/>
          <line x1="298" y1="26" x2="399" y2="26"/>
          <line x1="26" y1="399" x2="172" y2="399"/>
          <line x1="252" y1="399" x2="399" y2="399"/>
          <line x1="26" y1="26" x2="26" y2="399"/>
          <line x1="399" y1="26" x2="399" y2="399"/>
          <line x1="0" y1="0" x2="26" y2="26"/>
          <line x1="425" y1="0" x2="399" y2="26"/>
          <line x1="0" y1="425" x2="26" y2="399"/>
          <line x1="425" y1="425" x2="399" y2="399"/>
        </g>
      </svg>

      <div class="quote-card__tag">#STEELOUTLOOK</div>

      <h1 class="quote-card__quote">
        <span class="quote-card__line quote-card__line--lead">Prioritize</span>
        <span class="quote-card__line quote-card__line--join">and</span>
        <span class="quote-card__line quote-card__line--close">Execute</span>
      </h1>

      <div class="quote-card__brand">SO</div>
    </section>
  </main>
</body>
</html>
```